Audio Tour Poster

I need a poster to show information on a audio tour ... walk ... bike etc ... the poster needs to be generic so that it could be used for several projects ... a space needs to be left to add a tour title and another area where a tri fold brochure can be placed for people to access ... the tri fold poster will be based on 8.5 x 14 inch legal size ...

The size of the final poster will be 18x 24 inches ... an example of a audio tour can be found at
http://trallexo.com/walk/568 or http://trallexo.com/walk/2507

Industry/Entity Type

Legal

```html
<!DOCTYPE html>
<html lang="en">
<head>
<meta charset="UTF-8">
<title>Audio Tour Poster</title>
<link rel="stylesheet" href="https://fonts.googleapis.com/css2?family=Marcellus&family=Tenor+Sans&display=swap">
<style>
  :root {
    --page: #ffffff;
    --sky: #d3e9e2;
    --earth: #47300b;
    --foliage: #86a845;
    --foliage-light: #b9cf8c;
    --holder-back: #ffffff;
    --holder-front: rgba(220, 220, 220, 0.75);
    --holder-edge: #3a2a10;
    --on-earth: #ffffff;
  }
  html, body {
    margin: 0;
    padding: 0;
    width: 1200px;
    height: 1000px;
    overflow: hidden;
    background: var(--page);
  }
  .poster {
    position: absolute;
    left: 297px;
    top: 82px;
    width: 621px;
    height: 829px;
    background: var(--sky);
    overflow: hidden;
    color: var(--earth);
    font-family: "Marcellus", serif;
  }
  .headphones {
    position: absolute;
    left: 265px;
    top: 44px;
    width: 92px;
    height: 94px;
  }
  .title {
    position: absolute;
    left: 0;
    width: 100%;
    top: 150px;
    margin: 0;
    text-align: center;
    font-weight: 400;
    font-size: 84px;
    line-height: 76px;
    letter-spacing: 2px;
  }
  .modes {
    position: absolute;
    left: 0;
    width: 100%;
    top: 318px;
    margin: 0;
    text-align: center;
    font-weight: 400;
    font-size: 39px;
    letter-spacing: 1.5px;
    font-style: italic;
  }
  .features {
    position: absolute;
    left: 0;
    width: 100%;
    top: 379px;
    margin: 0;
    text-align: center;
    font-family: "Tenor Sans", sans-serif;
    font-size: 16px;
    line-height: 21px;
  }
  .scene {
    position: absolute;
    left: 0;
    top: 400px;
    width: 100%;
    height: 306px;
    background: linear-gradient(180deg, var(--foliage-light) 0%, var(--foliage) 45%, var(--foliage) 100%);
    clip-path: polygon(0 30%, 8% 20%, 18% 45%, 35% 55%, 65% 55%, 82% 40%, 92% 18%, 100% 10%, 100% 100%, 0 100%);
  }
  .ground {
    position: absolute;
    left: 0;
    bottom: 0;
    width: 100%;
    height: 124px;
    background: var(--earth);
  }
  .brochure-slot {
    position: absolute;
    left: 230px;
    top: 465px;
    width: 161px;
    height: 276px;
    background: var(--holder-back);
    border: 1px solid #b0b0b0;
    box-sizing: border-box;
  }
  .brochure-pocket {
    position: absolute;
    left: 224px;
    top: 537px;
    width: 172px;
    height: 216px;
    background: var(--holder-front);
    border: 1px solid var(--holder-edge);
    box-sizing: border-box;
  }
  .tour-name {
    position: absolute;
    left: 0;
    width: 100%;
    top: 764px;
    margin: 0;
    text-align: center;
    color: var(--on-earth);
    font-weight: 400;
    font-size: 27px;
    letter-spacing: 0.5px;
  }
  .speaker {
    position: absolute;
    top: 767px;
    width: 52px;
    height: 40px;
  }
  .speaker--left { left: 27px; }
  .speaker--right { left: 542px; transform: scaleX(-1); }
</style>
</head>
<body>
  <main class="poster">
    <svg class="headphones" viewBox="0 0 92 94" aria-hidden="true">
      <path d="M6 60 V44 A40 40 0 0 1 86 44 V60" fill="none" stroke="var(--earth)" stroke-width="4"/>
      <rect x="2" y="44" width="12" height="48" rx="4" fill="var(--earth)"/>
      <rect x="78" y="44" width="12" height="48" rx="4" fill="var(--earth)"/>
    </svg>

    <h1 class="title">AUDIO<br>TOUR</h1>
    <p class="modes">WALK, RIDE, DRIVE</p>
    <p class="features">MP3 downloads direct to your smartphone<br>Geopositioning gives you information<br>at the right time</p>

    <div class="scene" role="img" aria-label="Illustration of trees with silhouettes of walkers, a child and a cyclist on a path"></div>
    <div class="ground"></div>

    <div class="brochure-slot" aria-label="Brochure holder"></div>
    <div class="brochure-pocket"></div>

    <svg class="speaker speaker--left" viewBox="0 0 52 40" aria-hidden="true">
      <path d="M2 13 H10 L22 3 V37 L10 27 H2 Z" fill="var(--on-earth)"/>
      <path d="M28 12 A10 10 0 0 1 28 28" fill="none" stroke="var(--on-earth)" stroke-width="2.5"/>
      <path d="M34 7 A16 16 0 0 1 34 33" fill="none" stroke="var(--on-earth)" stroke-width="2.5"/>
      <path d="M40 2 A22 22 0 0 1 40 38" fill="none" stroke="var(--on-earth)" stroke-width="2.5"/>
    </svg>
    <p class="tour-name">This tour lorem ipsum dolor</p>
    <svg class="speaker speaker--right" viewBox="0 0 52 40" aria-hidden="true">
      <path d="M2 13 H10 L22 3 V37 L10 27 H2 Z" fill="var(--on-earth)"/>
      <path d="M28 12 A10 10 0 0 1 28 28" fill="none" stroke="var(--on-earth)" stroke-width="2.5"/>
      <path d="M34 7 A16 16 0 0 1 34 33" fill="none" stroke="var(--on-earth)" stroke-width="2.5"/>
      <path d="M40 2 A22 22 0 0 1 40 38" fill="none" stroke="var(--on-earth)" stroke-width="2.5"/>
    </svg>
  </main>
</body>
</html>
```